Pine Ridge Dwellings Stationary and Simplified Embroidery Contest
Business Card, Letterhead, Envelope, Note Pad, Sticker, Embroidery
Pine Ridge Dwellings Stationary and Simplified Embroidery Contest -
Creative Brief
Professional
Wendell Marsh
Construction Manager
4812 Galloway Street Edmonton AB T5K 3R8
wendell@pineridgedwellings.example
www.pineridgedwellings.example
Please include some with light backgrounds as well as dark options... we want to be able to print a few cards so that not every card we hand out is the same! I would like to have 4-6 business card designs. The embroidery part would just be a simplified logo.
Comments/Blank space for notes to written on the business card. We have looked at a few designs for business cards and like the Logo and Name on the front with all the details on the back, but do be creative with this is by no means a rule!

```html
<!DOCTYPE html>
<html lang="en">
<head>
<meta charset="utf-8">
<title>Pine Ridge Dwellings Stationery</title>
<link href="https://fonts.googleapis.com/css2?family=Cinzel:wght@400;600&family=Lato:wght@400;700&display=swap" rel="stylesheet">
<style>
:root{
  --board:#d4b384;
  --paper:#ffffff;
  --orange:#e3931f;
  --orange-dark:#b86f12;
  --charcoal:#2b2724;
  --olive:#5e6a3c;
  --grey:#8a8580;
  --faint:rgba(227,147,31,.14);
  --label:#3a2f22;
}
*{box-sizing:border-box;margin:0;padding:0}
html,body{width:1200px;height:727px;overflow:hidden}
body{background:var(--board);font-family:'Lato',Arial,sans-serif;color:var(--charcoal);position:relative}
.piece{position:absolute;background:var(--paper);box-shadow:0 2px 5px rgba(0,0,0,.35);overflow:hidden}
.label{position:absolute;font-size:7px;font-weight:700;color:var(--label);white-space:nowrap;z-index:5}
.brand{font-family:'Cinzel',Georgia,serif;font-weight:600;color:var(--charcoal);text-align:center;line-height:1.1;position:relative;z-index:2}
.brand-dot{display:block;margin:0 auto 3px;border-radius:50%;background:var(--orange)}
.card{width:118px;height:68px}
.card .brand{position:absolute;left:0;right:0;top:16px;font-size:7px}
.card .brand-dot{width:16px;height:16px}
.card-band{position:absolute;left:0;right:0;bottom:0;height:10px;background:var(--orange)}
.card-band.grey{background:var(--grey)}
.card-back{padding:8px 9px;font-size:5px;line-height:1.5}
.card-back .who{font-family:'Cinzel',Georgia,serif;font-size:7px;font-weight:600}
.card-back .role{color:var(--orange-dark);margin-bottom:3px}
.card-back .mini{font-family:'Cinzel',Georgia,serif;font-size:5.5px;font-weight:600;position:absolute;right:8px;top:8px;color:var(--orange-dark)}
.card-swoosh{position:absolute;left:0;top:0}
.card-lg{width:122px;height:80px}
.card-lg .brand{position:absolute;left:0;right:0;top:14px;font-size:7.5px}
.card-lg .brand-dot{width:26px;height:26px}
.card-lg.orange{background:var(--orange)}
.card-lg.orange .brand-dot{background:var(--charcoal)}
.card-lg .note-lines{position:absolute;left:10px;right:10px;top:14px}
.card-lg .note-lines i{display:block;height:12px;border-bottom:1px solid #cfcac4}
.watermark{position:absolute;border-radius:50%;border:14px solid var(--faint)}
.watermark-name{position:absolute;font-family:'Cinzel',Georgia,serif;font-weight:600;color:var(--faint);white-space:nowrap;transform:rotate(-90deg);transform-origin:left top}
.sheet{width:332px;height:414px;top:300px}
.sheet .brand{position:absolute;left:0;right:0;top:22px;font-size:12px}
.sheet .brand-dot{width:28px;height:28px}
.sheet .watermark-name{left:304px;top:405px;font-size:22px}
.sheet-foot{position:absolute;left:16px;right:16px;bottom:10px;font-size:5px;color:var(--grey);display:flex;justify-content:space-between}
.form{position:absolute;left:18px;right:30px;top:86px;border:1px solid #9a948e;font-size:6px;background:var(--paper)}
.form-row{display:flex;border-bottom:1px solid #9a948e;height:15px}
.form-row span{flex:1;padding:3px 4px;border-right:1px solid #9a948e}
.form-row span:last-child{border-right:0}
.form-no{position:absolute;right:30px;top:76px;font-size:6px}
.checks{position:absolute;left:18px;right:30px;top:166px;display:flex;justify-content:space-between;font-size:5.5px}
.checks span::before{content:"";display:inline-block;width:5px;height:5px;border:1px solid #777;margin-right:2px;vertical-align:-1px}
.env-front{left:740px;top:134px;width:448px;height:212px}
.env-front .brand{position:absolute;left:20px;top:16px;font-size:8px;text-align:left}
.env-front .brand-dot{width:22px;height:22px;margin:0 0 3px}
.env-front .addr{position:absolute;left:20px;top:58px;font-size:5.5px;line-height:1.5}
.env-back{left:782px;width:394px;height:118px}
.env-back svg{position:absolute;left:0;top:0}
.env-back .brand{position:absolute;left:0;right:0;top:74px;font-size:6px}
.env-back .brand-dot{width:10px;height:10px}
</style>
</head>
<body>

<div class="label" style="left:45px;top:10px">Business Card Option 1 (Front)</div>
<div class="piece card" style="left:30px;top:22px"><div class="brand"><span class="brand-dot"></span>Pine Ridge Dwellings</div><div class="card-band"></div></div>

<div class="label" style="left:186px;top:10px">Business Card Option 1 (Back)</div>
<div class="piece card card-back" style="left:170px;top:22px"><div class="mini">Pine Ridge</div><div class="who">Wendell Marsh</div><div class="role">Construction Manager</div>4812 Galloway Street Edmonton AB T5K 3R8<br>T 780 555 0142<br>wendell@pineridgedwellings.example<br>www.pineridgedwellings.example</div>

<div class="label" style="left:326px;top:10px">Business Card Option 2 (Front)</div>
<div class="piece card" style="left:310px;top:22px"><div class="brand"><span class="brand-dot"></span>Pine Ridge Dwellings</div><div class="card-band grey"></div></div>

<div class="label" style="left:466px;top:10px">Business Card Option 2 (Back)</div>
<div class="piece card card-back" style="left:450px;top:22px"><div class="who">Wendell Marsh</div><div class="role">Construction Manager</div>4812 Galloway Street Edmonton AB T5K 3R8<br>T 780 555 0142<br>wendell@pineridgedwellings.example<br>www.pineridgedwellings.example<div class="card-band grey" style="height:5px"></div></div>

<div class="label" style="left:616px;top:10px">Business Card Option 3 (Front)</div>
<div class="piece card" style="left:600px;top:22px"><div class="brand"><span class="brand-dot"></span>Pine Ridge Dwellings</div><div class="card-band" style="height:6px"></div></div>

<div class="label" style="left:766px;top:10px">Business Card Option 3 (Back)</div>
<div class="piece card card-back" style="left:750px;top:22px"><div class="who">Wendell Marsh</div><div class="role">Construction Manager</div>4812 Galloway Street Edmonton AB T5K 3R8<br>T 780 555 0142<br>wendell@pineridgedwellings.example<br>www.pineridgedwellings.example</div>

<div class="label" style="left:916px;top:10px">Business Card Option 4 (Front)</div>
<div class="piece card" style="left:900px;top:22px"><svg class="card-swoosh" width="118" height="68"><path d="M0 64 Q60 58 118 46 L118 68 L0 68Z" fill="#e3931f"/></svg><div class="brand"><span class="brand-dot"></span>Pine Ridge Dwellings</div></div>

<div class="label" style="left:1060px;top:10px">Business Card Option 4 (Back)</div>
<div class="piece card card-back" style="left:1050px;top:22px"><svg class="card-swoosh" width="118" height="68"><path d="M0 68 Q60 66 118 61 L118 68Z" fill="#e3931f"/></svg><div class="who">Wendell Marsh</div><div class="role">Construction Manager</div>4812 Galloway Street Edmonton AB T5K 3R8<br>T 780 555 0142<br>wendell@pineridgedwellings.example<br>www.pineridgedwellings.example</div>

<div class="label" style="left:30px;top:112px">Business Card Option 5 (Front)</div>
<div class="piece card-lg" style="left:20px;top:124px"><div class="brand"><span class="brand-dot"></span>Pine Ridge Dwellings</div></div>

<div class="label" style="left:165px;top:112px">Business Card Option 5 (Back)</div>
<div class="piece card-lg" style="left:155px;top:124px"><div class="note-lines"><i></i><i></i><i></i><i></i></div></div>

<div class="label" style="left:300px;top:112px">Business Card Option 6 (Front)</div>
<div class="piece card-lg" style="left:290px;top:124px"><div class="brand"><span class="brand-dot"></span>Pine Ridge Dwellings</div></div>

<div class="label" style="left:435px;top:112px">Business Card Option 6 (Back)</div>
<div class="piece card-lg orange" style="left:425px;top:124px"><div class="brand"><span class="brand-dot"></span>Pine Ridge Dwellings</div></div>

<div class="label" style="left:930px;top:122px">Envelope Option 1</div>
<div class="piece env-front">
  <div class="watermark" style="left:240px;top:30px;width:170px;height:170px"></div>
  <div class="brand"><span class="brand-dot"></span>Pine Ridge Dwellings</div>
  <div class="addr">4812 Galloway Street<br>Edmonton AB T5K 3R8</div>
</div>

<div class="piece sheet" style="left:24px">
  <div class="watermark" style="left:40px;top:190px;width:250px;height:250px"></div>
  <div class="watermark-name">Pine Ridge Dwellings</div>
  <div class="brand"><span class="brand-dot"></span>Pine Ridge Dwellings</div>
  <div class="form-no">1001</div>
  <div class="form">
    <div class="form-row"><span>To:</span><span>Date:</span></div>
    <div class="form-row"><span>From:</span><span>Time:</span></div>
    <div class="form-row"><span>Phone:</span><span>Ext:</span></div>
    <div class="form-row" style="border-bottom:0"><span>Email:</span><span>Job:</span></div>
  </div>
  <div class="checks"><span>Urgent</span><span>Call Back</span><span>Please Review</span><span>Return Call</span><span>Will Visit</span></div>
  <div class="sheet-foot"><span>4812 Galloway Street Edmonton AB T5K 3R8 &nbsp; T 780 555 0142</span><span>www.pineridgedwellings.example</span></div>
</div>

<div class="label" style="left:520px;top:290px">Letterhead</div>
<div class="piece sheet" style="left:380px">
  <div class="watermark" style="left:40px;top:190px;width:250px;height:250px"></div>
  <div class="watermark-name">Pine Ridge Dwellings</div>
  <div class="brand"><span class="brand-dot"></span>Pine Ridge Dwellings</div>
  <div class="sheet-foot"><span>4812 Galloway Street Edmonton AB T5K 3R8 &nbsp; T 780 555 0142</span><span>www.pineridgedwellings.example</span></div>
</div>

<div class="label" style="left:930px;top:360px">Envelope Option 1 (Back)</div>
<div class="piece env-back" style="top:372px">
  <svg width="394" height="118"><path d="M0 0 L394 0 L240 58 Q197 72 154 58Z" fill="#fff" stroke="#ccc"/><path d="M0 118 L170 62 M394 118 L224 62" stroke="#ddd"/></svg>
  <div class="brand"><span class="brand-dot"></span>Pine Ridge Dwellings</div>
</div>

<div class="label" style="left:930px;top:476px">Envelope Option 2 (Back)</div>
<div class="piece env-back" style="top:488px">
  <svg width="394" height="118"><path d="M0 0 L394 0 L240 58 Q197 72 154 58Z" fill="#5e6a3c"/><path d="M0 118 L170 62 M394 118 L224 62" stroke="#ddd"/></svg>
  <div class="brand"><span class="brand-dot"></span>Pine Ridge Dwellings</div>
</div>

<div class="label" style="left:930px;top:592px">Envelope Option 3 (Back)</div>
<div class="piece env-back" style="top:604px">
  <svg width="394" height="118"><path d="M0 0 L394 0 L240 58 Q197 72 154 58Z" fill="#e3931f"/><path d="M0 118 L170 62 M394 118 L224 62" stroke="#ddd"/></svg>
  <div class="brand"><span class="brand-dot"></span>Pine Ridge Dwellings</div>
</div>

</body>
</html>
```